Velm Otter

I want a design for a website where users can insert products URLs from different sites and the user will get notified by email when that product's price changes.

On the homepage I'd like a big input where the user can insert a product's URL. On the same page the following will appear:
- my products that I follow (options: share, buy, unfollow) + it's current price and deviation from last time it's price has changed (I may have many products that I follow, so maybe a table layout would be wise. - just a suggestion)
- products that other people follow (options: follow). If my Quillmark friends follow a certain product, I can see their photo(eg: friend1, friend2 and 5 others are following this product) (also, may people may follow a product.)

On the login page I can register using user / pass or using Quillmark

The 3rd page is the product's page. Once I click on any product I go to this page. On this page I can see:
- picture, name and price and no of people following this product
- a chart with the product's price over the last 30 days
- list with friends that follow this product (when logged in)
- product options: follow / unfollow, share, buy

Then I want the design for an email template that I send when 1 or more prices of a user's products change.

Nice to have: want level for product - describes how much wanted is a product after a certain internal algorithm

NB:
- flat design (not really pivra, something more like the new Zyx interface - just a suggestion)
- I'd prefer a red theme (based on the idea that the site will be represented by a rooster)
- don't forget the design for basic elements: loading screen, popup, alert, messages, etc

I've posted an initial prototype with what I'd like the design to contain.

• - flat design
- must be simple. much white space
• as few gradients as possible

```html
<!DOCTYPE html>
<html lang="en">
<head>
<meta charset="utf-8">
<title>Velm Otter – My Products</title>
<link href="https://fonts.googleapis.com/css2?family=Open+Sans:wght@400;600;700&display=swap" rel="stylesheet">
<style>
:root{
  --page:#f4f4f4;
  --white:#ffffff;
  --red:#d0202a;
  --green:#4a8a10;
  --grey:#a8a8a8;
  --grey-soft:#e2e2e2;
  --line:#dcdcdc;
  --ink:#1c1c1c;
  --ink-soft:#444444;
  --muted:#9a9a9a;
}
*{box-sizing:border-box;margin:0;padding:0}
html,body{width:909px;height:1200px;overflow:hidden;background:var(--page)}
body{font-family:"Open Sans",Arial,sans-serif;color:var(--ink);position:relative}
.page{position:relative;width:909px;height:1200px}

/* header */
.brand{position:absolute;left:79px;top:38px;display:flex;align-items:center;gap:8px;font-size:21px;font-weight:600;color:var(--red)}
.brand .mark{width:12px;height:12px;border-radius:50%;background:var(--red)}
.main-nav{position:absolute;left:543px;top:25px;width:217px;height:28px;background:var(--red);display:flex;align-items:center;justify-content:center;font-size:10.5px;color:var(--white)}
.main-nav span.sep{margin:0 9px;opacity:.8}
.social{position:absolute;top:25px;left:775px;display:flex;gap:3px}
.social .dot{width:25px;height:25px;border-radius:50%;background:#9d9d9d}

/* url bar */
.url-bar{position:absolute;left:79px;top:80px;width:623px;height:61px;background:var(--grey);padding:8px}
.url-field{height:45px;background:var(--white);border:1px solid #cfcfcf;display:flex}
.url-field .placeholder{flex:1;font-size:13px;color:#8a8a8a;padding:14px 16px}
.url-field .follow-btn{width:95px;background:#e9e9e9;border-left:1px solid #c6c6c6;font-size:14px;color:#333;display:flex;align-items:center;justify-content:center}
.login-btn{position:absolute;left:707px;top:80px;width:120px;height:61px;background:var(--green);color:var(--white);font-size:13.5px;display:flex;align-items:center;justify-content:center}

/* sections */
.section-title{position:absolute;left:79px;font-size:17px;font-weight:700}

/* followed product cards */
.product-card{position:absolute;left:79px;width:751px;height:142px;background:var(--white);border:1px solid var(--line)}
.product-card .photo{position:absolute;left:25px;top:18px;width:129px;height:102px}
.product-card .name{position:absolute;left:164px;top:16px;font-size:13.5px}
.price-row{position:absolute;left:164px;top:40px;display:flex;gap:3px}
.price{width:62px;height:22px;background:var(--red);color:var(--white);font-size:10px;display:flex;align-items:center;justify-content:center}
.change{width:65px;height:22px;background:var(--grey);color:var(--white);font-size:10px;display:flex;align-items:center;justify-content:center;gap:4px}
.product-card .desc{position:absolute;left:165px;top:76px;width:300px;font-size:9.6px;line-height:14px;color:var(--ink-soft)}
.buy-btn{position:absolute;left:498px;top:18px;width:102px;height:21px;background:var(--green);color:var(--white);font-size:9.8px;font-weight:700;display:flex;align-items:center;justify-content:center}
.action{position:absolute;top:21px;display:flex;align-items:center;gap:5px;font-size:10px;color:var(--ink-soft)}
.action.share{left:617px}
.action.unfollow{left:670px}

/* load more */
.divider{position:absolute;left:79px;width:751px;height:1px;background:var(--line)}
.load-more{position:absolute;left:380px;width:143px;height:44px;background:var(--grey-soft);color:var(--muted);font-size:13px;display:flex;align-items:center;justify-content:center}

/* other users grid */
.user-card{position:absolute;top:808px;width:180px;height:230px;background:var(--white);border:1px solid var(--line)}
.user-card .photo{position:absolute;left:25px;top:19px;width:129px;height:102px}
.user-card .name{position:absolute;left:0;right:0;top:130px;text-align:center;font-size:10px}
.followers{position:absolute;left:8px;top:157px;display:flex;gap:4px}
.friend{width:38px;text-align:center}
.friend .avatar{width:38px;height:38px}
.friend .who{font-size:6.5px;color:var(--muted);margin-top:3px}
.more{width:38px;height:38px;background:var(--grey-soft);font-size:10px;color:var(--ink-soft);display:flex;align-items:center;justify-content:center}

/* footer */
.footer{position:absolute;left:0;right:0;top:1159px;text-align:center;font-size:10px;color:var(--ink)}
.footer .sep{margin:0 6px;color:var(--muted)}
.footer .link{color:var(--red)}
</style>
</head>
<body>
<div class="page">

  <header>
    <div class="brand"><span class="mark"></span>Velm Otter</div>
    <nav class="main-nav"><span>Home</span><span class="sep">|</span><span>Browse Products</span><span class="sep">|</span><span>Contact</span></nav>
    <div class="social" aria-label="Quillmark and Chirpline"><span class="dot"></span><span class="dot"></span></div>
  </header>

  <div class="url-bar">
    <div class="url-field"><span class="placeholder">Enter a product’s url</span><span class="follow-btn">Follow</span></div>
  </div>
  <div class="login-btn">Login / Register</div>

  <h2 class="section-title" style="top:159px">My Products</h2>

  <article class="product-card" style="top:201px">
    <div class="photo" role="img" aria-label="Bundle of wooden pencils" style="background:linear-gradient(135deg,#ededeb,#d9d2c4)"></div>
    <div class="name">Special wood pencils</div>
    <div class="price-row"><span class="price">450 USD</span><span class="change">+4 USD <svg width="6" height="9" viewBox="0 0 6 9"><path d="M3 9V1M0.5 3.5L3 1l2.5 2.5" stroke="#fff" fill="none"/></svg></span></div>
    <p class="desc">Maecenas placerat, nisl at consequat rhoncus, sem nunc gravida justo, quis eleifend arcu velit</p>
    <div class="buy-btn">Buy This Product</div>
    <div class="action share"><svg width="12" height="12" viewBox="0 0 12 12"><rect x="0.5" y="0.5" width="11" height="11" fill="none" stroke="#999"/><path d="M3 6l2 2 4-5" stroke="#999" fill="none"/></svg>Share</div>
    <div class="action unfollow"><svg width="13" height="12" viewBox="0 0 13 12"><rect x="0.5" y="0.5" width="9" height="11" fill="none" stroke="#999"/><path d="M4 6h8M10 4l2 2-2 2" stroke="#999" fill="none"/></svg>Unfollow</div>
  </article>

  <article class="product-card" style="top:361px">
    <div class="photo" role="img" aria-label="Grey dress with laces" style="background:linear-gradient(135deg,#ecebe8,#a8a295)"></div>
    <div class="name">Modern dress with laces</div>
    <div class="price-row"><span class="price">450 USD</span><span class="change">+4 USD <svg width="6" height="9" viewBox="0 0 6 9"><path d="M3 9V1M0.5 3.5L3 1l2.5 2.5" stroke="#fff" fill="none"/></svg></span></div>
    <p class="desc">Maecenas placerat, nisl at consequat rhoncus, sem nunc gravida justo, quis eleifend arcu velit</p>
    <div class="buy-btn">Buy This Product</div>
    <div class="action share"><svg width="12" height="12" viewBox="0 0 12 12"><rect x="0.5" y="0.5" width="11" height="11" fill="none" stroke="#999"/><path d="M3 6l2 2 4-5" stroke="#999" fill="none"/></svg>Share</div>
    <div class="action unfollow"><svg width="13" height="12" viewBox="0 0 13 12"><rect x="0.5" y="0.5" width="9" height="11" fill="none" stroke="#999"/><path d="M4 6h8M10 4l2 2-2 2" stroke="#999" fill="none"/></svg>Unfollow</div>
  </article>

  <article class="product-card" style="top:524px">
    <div class="photo" role="img" aria-label="Gold plated cuff bracelet" style="background:linear-gradient(135deg,#f1f0ee,#d8c3a8)"></div>
    <div class="name">Gold plated vintage breclet</div>
    <div class="price-row"><span class="price">450 USD</span><span class="change">+4 USD <svg width="6" height="9" viewBox="0 0 6 9"><path d="M3 9V1M0.5 3.5L3 1l2.5 2.5" stroke="#fff" fill="none"/></svg></span></div>
    <p class="desc" style="width:270px">Maecenas placerat, nisl at consequat rhoncus, sem nunc gravida justo, quis eleifend arcu velit</p>
    <div class="buy-btn">Buy This Product</div>
    <div class="action share"><svg width="12" height="12" viewBox="0 0 12 12"><rect x="0.5" y="0.5" width="11" height="11" fill="none" stroke="#999"/><path d="M3 6l2 2 4-5" stroke="#999" fill="none"/></svg>Share</div>
    <div class="action unfollow"><svg width="13" height="12" viewBox="0 0 13 12"><rect x="0.5" y="0.5" width="9" height="11" fill="none" stroke="#999"/><path d="M4 6h8M10 4l2 2-2 2" stroke="#999" fill="none"/></svg>Unfollow</div>
  </article>

  <div class="divider" style="top:689px"></div>
  <div class="load-more" style="top:689px">Load more products</div>

  <h2 class="section-title" style="top:762px">Products from other Users</h2>

  <article class="user-card" style="left:79px">
    <div class="photo" role="img" aria-label="Spool of cotton twine" style="background:linear-gradient(180deg,#e9e7e3,#d6d0c6)"></div>
    <div class="name">Special wood pencils</div>
    <div class="followers">
      <div class="friend"><div class="avatar" role="img" aria-label="Friend photo" style="background:#5d4a3c"></div><div class="who">Orvin</div></div>
      <div class="friend"><div class="avatar" role="img" aria-label="Friend photo" style="background:#6e6a64"></div><div class="who">Temo</div></div>
      <div class="friend"><div class="avatar" role="img" aria-label="Friend photo" style="background:#5a6a7a"></div><div class="who">Safi</div></div>
      <div class="more">+10</div>
    </div>
  </article>

  <article class="user-card" style="left:269px">
    <div class="photo" role="img" aria-label="Lace socks with brown shoes" style="background:linear-gradient(180deg,#c9c9c9,#b3aaa0)"></div>
    <div class="name">Modern dress with laces</div>
    <div class="followers">
      <div class="friend"><div class="avatar" role="img" aria-label="Friend photo" style="background:#5d4a3c"></div><div class="who">Orvin</div></div>
      <div class="friend"><div class="avatar" role="img" aria-label="Friend photo" style="background:#6e6a64"></div><div class="who">Temo</div></div>
      <div class="friend"><div class="avatar" role="img" aria-label="Friend photo" style="background:#5a6a7a"></div><div class="who">Safi</div></div>
      <div class="more">+10</div>
    </div>
  </article>

  <article class="user-card" style="left:459px">
    <div class="photo" role="img" aria-label="White cup with a locket" style="background:linear-gradient(180deg,#eeeeee,#dcd8d0)"></div>
    <div class="name">Set of pilows</div>
    <div class="followers">
      <div class="friend"><div class="avatar" role="img" aria-label="Friend photo" style="background:#5d4a3c"></div><div class="who">Orvin</div></div>
      <div class="friend"><div class="avatar" role="img" aria-label="Friend photo" style="background:#6e6a64"></div><div class="who">Temo</div></div>
      <div class="friend"><div class="avatar" role="img" aria-label="Friend photo" style="background:#5a6a7a"></div><div class="who">Safi</div></div>
      <div class="more">+10</div>
    </div>
  </article>

  <article class="user-card" style="left:650px">
    <div class="photo" role="img" aria-label="Stone bead bracelet" style="background:linear-gradient(180deg,#e9e6e1,#d8d0c4)"></div>
    <div class="name">Gold plated vintage breclet</div>
    <div class="followers">
      <div class="friend"><div class="avatar" role="img" aria-label="Friend photo" style="background:#5d4a3c"></div><div class="who">Orvin</div></div>
      <div class="friend"><div class="avatar" role="img" aria-label="Friend photo" style="background:#6e6a64"></div><div class="who">Temo</div></div>
      <div class="friend"><div class="avatar" role="img" aria-label="Friend photo" style="background:#5a6a7a"></div><div class="who">Safi</div></div>
      <div class="more">+10</div>
    </div>
  </article>

  <div class="divider" style="top:1062px"></div>
  <div class="load-more" style="top:1062px">Load more products</div>

  <div class="divider" style="top:1138px"></div>
  <footer class="footer">© 2013 Velm Otter<span class="sep">|</span><span class="link">Disclaimer</span></footer>

</div>
</body>
</html>
```